Brookmere Joinery Design Upgrade

- This is for a layout design of the home page only. No coding required.

- The design should be based around the attached HPID (home page information design) I've attached both a JPEG of this
- Information only is in RED text. Copy to go on the design in BLACK text. Some instructions are in the HPID. Please be creative!
- The design needs to be clean and spacious
- Use the logo provided. Please use the colours from the logos in the website design.
- I've attached some images to use as examples to use for home page gallery
- The product logos (Fenwyk, Clearbirch etc) showed in the HPV can be googled for a higher quality image if required.
- The header can be changed/altered - just needs to have all information as per logo, along with the phone number.

- Expected standard of design examples: (Please DO NOT copy these exactly – they are just examples)
http://www.palomir-works.co.nz/
http://www.hushlinecorp.co.nz/
http://www.dunkettle.co.nz/

Width of content will be 1100 pixels when implemented as a web page. Header height (without nav bar) 150-160 pixels.

The winning PSD file will have to be provided as follows…
1. Canvas size of 2000px x 2000px - 72ppi in Adobe Photoshop (CS5 compatible)
2. Width of content section is 1100px wide - centered in the canvas
3. Any button rollovers/hovers in the PSD as hidden layers.
4. All fonts used must be Google fonts (except for the header fonts).
5. You will need to supply the chosen home page plus one example page (example page as a style guide for how all other pages will look). Example page is only the header and navigational bar at the top, an empty sector in the middle with a column (180 px wide) which can be left or right aligned which means the main sector is 920 pixels wide, and then the footer at the bottom of the page.

```html
<!DOCTYPE html>
<html lang="en">
<head>
<meta charset="utf-8">
<title>Brookmere Joinery — Home</title>
<link href="https://fonts.googleapis.com/css2?family=Open+Sans:ital,wght@0,400;0,600;0,700;0,800;1,400&display=swap" rel="stylesheet">
<style>
:root{
  --red:#e2231a;
  --navy:#16306e;
  --navy-dark:#0f2152;
  --ink:#333;
  --muted:#777;
  --page:#ececec;
  --panel:#fff;
  --line:#d6d6d6;
  --gold:#f4c20d;
}
*{box-sizing:border-box;margin:0;padding:0}
html,body{width:733px;height:1200px;overflow:hidden}
body{background:var(--page);font-family:"Open Sans",Arial,sans-serif;color:var(--ink);position:relative}
.header{position:absolute;left:0;top:0;width:733px;height:86px;background:var(--panel)}
.brand{position:absolute;left:28px;top:10px;width:112px;height:56px;background:var(--navy);color:#fff;padding:7px 8px;font-weight:800;line-height:1}
.brand .name{font-size:15px;letter-spacing:.5px}
.brand .sub{font-size:12px;margin-top:3px}
.brand .tag{font-size:6px;font-weight:400;margin-top:5px;letter-spacing:.5px}
.contact{position:absolute;left:400px;top:14px;text-align:right;width:200px}
.contact .place{font-size:7px;color:var(--muted);letter-spacing:.5px}
.contact .phone{font-size:20px;font-weight:700;color:var(--red);line-height:1.2}
.contact .strip{display:inline-block;margin-top:3px;background:var(--red);color:#fff;font-size:6px;padding:2px 6px;letter-spacing:.4px}
.partner{position:absolute;left:618px;top:22px;display:flex;align-items:center;gap:6px;font-weight:700;font-size:13px;color:var(--navy)}
.partner i{display:block;width:12px;height:12px;background:var(--red)}
.nav{position:absolute;left:0;top:86px;width:733px;height:22px;background:var(--red);display:flex;padding-left:34px}
.nav a{color:#fff;font-size:7px;font-weight:600;text-decoration:none;padding:0 9px;line-height:22px;letter-spacing:.3px}
.nav a.on{background:#b8160f}
.main{position:absolute;left:28px;top:108px;width:677px;height:930px;background:var(--panel)}
.headline{position:absolute;left:16px;top:16px;font-size:17px;color:var(--ink);font-weight:400}
.headline b{color:var(--navy);font-weight:700}
.slider{position:absolute;left:16px;top:48px;width:645px;height:260px;background:linear-gradient(180deg,#c9d6e4 0%,#aebcc8 45%,#8d9a86 100%);border:1px solid var(--line)}
.quote{position:absolute;left:110px;top:48px;display:flex;font-size:9px;font-weight:700}
.quote span{padding:6px 8px}
.quote .a{background:var(--gold);color:var(--ink)}
.quote .b{background:var(--red);color:#fff}
.caption{position:absolute;right:0;bottom:14px;background:rgba(15,33,82,.85);color:#fff;font-weight:700;font-size:13px;padding:8px 14px 8px 40px}
.dots{position:absolute;left:14px;bottom:18px;display:flex;gap:5px}
.dots i{width:7px;height:7px;border-radius:50%;background:#fff;opacity:.6}
.dots i:first-child{opacity:1}
.logos{position:absolute;left:16px;top:326px;width:645px;height:58px;border-top:1px solid var(--line);border-bottom:1px solid var(--line);display:flex;justify-content:space-around;align-items:center}
.logos span{font-size:10px;font-weight:700;color:var(--navy);display:flex;align-items:center;gap:5px}
.logos i{width:9px;height:9px;background:var(--navy);display:block}
.cards{position:absolute;left:16px;top:412px;width:645px}
.card{position:absolute;width:205px;height:212px;border:1px solid var(--line);background:#fafafa}
.card h3{background:var(--navy);color:#fff;font-size:9px;font-weight:700;padding:6px 8px;letter-spacing:.3px}
.card em{display:block;font-size:8px;color:var(--ink);padding:6px 8px 4px}
.card .photo{margin:0 8px;height:100px;background:linear-gradient(160deg,#cfd9e2,#8e9ca6)}
.card p{font-size:6.4px;color:var(--muted);line-height:1.5;padding:7px 8px}
.footer{position:absolute;left:28px;top:1046px;width:677px;height:140px}
.footer h4{font-size:8px;font-weight:700;color:var(--ink);margin-bottom:5px}
.col{position:absolute;top:10px;font-size:6.5px;color:var(--muted);line-height:1.55}
.col ul{list-style:none}
.seal{position:absolute;left:470px;top:8px;width:52px;height:52px;border-radius:50%;background:var(--gold)}
.seal-text{position:absolute;left:534px;top:14px;width:120px;font-size:6.5px;color:var(--ink);line-height:1.5}
.legal{position:absolute;left:0;top:118px;width:677px;border-top:1px solid var(--line);padding-top:5px;font-size:5.5px;color:var(--muted);text-align:center}
</style>
</head>
<body>
<header class="header">
  <div class="brand"><div class="name">BROOKMERE</div><div class="sub">Joinery Ltd</div><div class="tag">DESIGN · BUILD · INSTALL</div></div>
  <div class="contact">
    <div class="place">UPPER HOLLOW · WELLINGTON</div>
    <div class="phone">(04) 555 0192</div>
    <div class="strip">EXCELLENCE | 26 HARBOURVIEW RD, UPPER HOLLOW</div>
  </div>
  <div class="partner"><i></i>Fenwyk</div>
</header>
<nav class="nav">
  <a class="on">HOME</a><a>ABOUT US</a><a>COMMERCIAL</a><a>NEW HOMES</a><a>REPLACEMENT JOINERY</a><a>DOUBLE GLAZING</a><a>CONSERVATORIES</a><a>GALLERY</a><a>GET A FREE QUOTE</a><a>CONTACT US</a>
</nav>
<main class="main">
  <h1 class="headline">Ensuring Style and Functionality with your <b>Aluminium Joinery</b></h1>
  <div class="slider" role="img" aria-label="Photo of a modern building with aluminium windows">
    <div class="quote"><span class="a">GET A FREE</span><span class="b">QUOTE FOR YOUR JOINERY NEEDS</span></div>
    <div class="dots"><i></i><i></i><i></i><i></i><i></i></div>
    <div class="caption">COMMERCIAL JOINERY</div>
  </div>
  <div class="logos">
    <span><i></i>Fenwyk</span><span><i></i>Clearbirch</span><span><i></i>Tallowby</span><span><i></i>Orrin Frames</span><span><i></i>Sealmark</span>
  </div>
  <div class="cards">
    <article class="card" style="left:0;top:0"><h3>NEW HOMES</h3><em>Building your dream home?</em><div class="photo" role="img" aria-label="Photo of a new home"></div><p>Brookmere Joinery provides a wide range of styles and finishes to help you get the perfect frames, from plain doors to sliding windows, all to suit your build.</p></article>
    <article class="card" style="left:220px;top:0"><h3>COMMERCIAL</h3><em>Improve the presentation of your business</em><div class="photo" role="img" aria-label="Photo of a commercial building"></div><p>Brookmere Joinery provides a wide range of styles and finishes to help you get the perfect frames, from shop fronts to office glazing, all made to last.</p></article>
    <article class="card" style="left:440px;top:0"><h3>REPLACEMENT JOINERY</h3><em>Tired of old windows and doors?</em><div class="photo" role="img" aria-label="Photo of replaced windows"></div><p>Brookmere Joinery provides a wide range of styles and finishes to help you replace worn timber frames with modern aluminium that is easy to care for.</p></article>
    <article class="card" style="left:0;top:232px"><h3>DOUBLE GLAZING</h3><em>Enjoy the many benefits of double glazing</em><div class="photo" role="img" aria-label="Photo of double glazed windows"></div><p>Brookmere Joinery provides a wide range of glazing options to keep your home warm, quiet and dry, from simple units to full thermal systems.</p></article>
    <article class="card" style="left:220px;top:232px"><h3>CONSERVATIONS</h3><em>Enjoy the sun all year round</em><div class="photo" role="img" aria-label="Photo of a glass conservatory"></div><p>Brookmere Joinery provides a wide range of conservatory styles and finishes to bring more light into your home, built to suit your space.</p></article>
  </div>
</main>
<footer class="footer">
  <div class="col" style="left:0"><h4>INFORMATION</h4><ul><li>HOME</li><li>ABOUT US</li><li>COMMERCIAL</li><li>NEW HOMES</li><li>REPLACEMENT JOINERY</li></ul></div>
  <div class="col" style="left:90px;top:25px"><ul><li>DOUBLE GLAZING</li><li>CONSERVATORIES</li><li>GALLERY</li><li>GET A FREE QUOTE</li><li>CONTACT US</li></ul></div>
  <div class="col" style="left:230px"><h4>CONTACT DETAILS</h4><ul><li>(04) 555 0192</li><li>(04) 555 0193</li><li>FAX: (04) 555 0194</li><li>Physical Address: 26 Harbourview Rd, Upper Hollow</li><li>Postal Address: PO Box 9050, Upper Hollow</li></ul></div>
  <div class="seal" role="img" aria-label="Warranty badge"></div>
  <div class="seal-text">We guarantee all our work; if there is ever a problem we will be back to sort it promptly.</div>
  <div class="legal">© 2024 Brookmere Joinery Ltd · Joinery &amp; glazing across the Upper Hollow and Wellington region · All rights reserved</div>
</footer>
</body>
</html>
```